Beauty Clinic Treatment Menu (Lumen Nails & Beauty)

Needing a treatment menu designed for a beauty clinic in Kiriwai, New Zealand. Like the colours grey, pink, white.
Elegant, Modern and feminine

Lumen Nails & Beauty
Karen Pell
Room3, 48 Tainui Street
Kiriwai
0273816240
Karen.lumen@mailbox.test
lumenbeauty.co.nz

Target Market(s)

Females

Industry/Entity Type

Beauty Salon

Font styles to use
Serif

Colors

Requirements
Must have
• Chatterly and Snapgrid logo

```html
<!DOCTYPE html>
<html lang="en">
<head>
<meta charset="utf-8">
<title>Lumen Nails &amp; Beauty – Treatment Menu</title>
<link href="https://fonts.googleapis.com/css2?family=Great+Vibes&family=Open+Sans:wght@400;600&display=swap" rel="stylesheet">
<style>
:root{
  --backdrop:#d5d5d8;
  --paper:#ffffff;
  --mist:#efeeef;
  --slate:#67636a;
  --rose:#d8aba0;
  --rosegold:#b98573;
  --ink:#3d3a3f;
}
*{margin:0;padding:0;box-sizing:border-box}
html,body{width:844px;height:1200px;overflow:hidden}
body{background:var(--backdrop);font-family:"Open Sans",Arial,sans-serif;color:var(--ink);position:relative}
.sheet{position:absolute;left:47px;width:749px;height:530px;background:var(--paper);box-shadow:0 8px 12px rgba(0,0,0,.18);overflow:hidden}
.sheet--outside{top:43px}
.sheet--inside{top:623px}
.panel{position:absolute;top:0;height:100%;width:250px;overflow:hidden}
.panel--1{left:0}.panel--2{left:250px}.panel--3{left:500px;width:249px}
.script{font-family:"Great Vibes",cursive;color:var(--rosegold);font-weight:400}
.photo{position:absolute}
.brand{font-family:"Open Sans",Arial,sans-serif;font-weight:600;color:var(--rosegold)}

/* outside: about */
.about-title{position:absolute;left:21px;top:36px;font-size:24px}
.about-copy{position:absolute;left:21px;right:18px;font-size:7.6px;line-height:12.4px;text-align:justify}
.about-copy--a{top:73px}.about-copy--b{top:162px}
.about-photo{left:0;top:330px;width:250px;height:200px;background:linear-gradient(160deg,#efe4de,#d9c6bf 55%,#c8aaa0)}
.ring{position:absolute;border-radius:50%;border:4px solid var(--rose);box-shadow:0 2px 5px rgba(0,0,0,.2)}
.ring--nails{left:7px;top:268px;width:112px;height:112px;background:linear-gradient(135deg,#e8d4cc,#b99387)}
.ring--eyes{left:133px;top:285px;width:92px;height:92px;background:linear-gradient(135deg,#f1e3da,#caa899)}

/* outside: contact */
.panel--2.outside{background:var(--mist)}
.logo-ring{position:absolute;left:78px;top:45px;width:94px;height:94px;border-radius:50%;border:1.5px solid var(--rosegold);display:flex;flex-direction:column;align-items:center;justify-content:center;background:var(--paper)}
.logo-ring .brand{font-size:20px;letter-spacing:1px}
.logo-ring small{font-size:5px;color:var(--rosegold)}
.quote-mark{position:absolute;left:0;right:0;top:168px;text-align:center;font-size:28px;color:var(--rose);font-family:Georgia,serif;font-weight:bold}
.testimonial{position:absolute;left:18px;right:18px;top:196px;text-align:center;font-style:italic;font-size:7.6px;line-height:12px;color:#6d6a70}
.call-title{position:absolute;left:0;right:0;top:262px;text-align:center;font-size:28px}
.pill{position:absolute;left:50%;transform:translateX(-50%);border:1.2px solid var(--rose);border-radius:10px;font-size:11px;padding:2px 16px;white-space:nowrap;display:flex;align-items:center;gap:6px}
.pill--phone{top:298px;color:var(--ink)}
.email{position:absolute;left:0;right:0;top:325px;text-align:center;font-size:9px;color:var(--rose)}
.address{position:absolute;left:0;right:0;top:408px;text-align:center;color:#fff;font-size:10.5px;line-height:14.5px;font-style:normal}
.socials{position:absolute;left:0;right:0;top:478px;display:flex;justify-content:center;gap:8px;color:#fff;font-size:8px;align-items:center;white-space:nowrap}
.social{display:flex;align-items:center;gap:3px}
.social i{display:inline-block;width:10px;height:10px;background:var(--rose);border-radius:2px}
.pill--web{top:496px;color:#fff;font-size:11.5px}

/* outside: cover */
.cover-logo{position:absolute;left:0;right:0;top:20px;text-align:center}
.cover-logo .brand{font-size:36px;letter-spacing:2px;display:block;line-height:44px}
.cover-logo small{font-size:7px;color:var(--rosegold)}
.cover-photo{left:0;top:80px;width:249px;height:340px;background:linear-gradient(150deg,#c9a79c,#8b6a6a 45%,#4d3a3f)}
.cover-title{position:absolute;left:0;right:0;top:440px;text-align:center;font-size:29px;color:var(--rose)}

/* inside menus */
.menu-title{font-size:23px;margin-bottom:4px}
.dark .menu-title{color:var(--rose)}
.menu-head{font-size:8px;color:var(--rose);text-transform:uppercase;margin:9px 0 4px}
.row{display:flex;font-size:8px;line-height:12.4px;white-space:nowrap}
.row .dots{flex:1;border-bottom:1px dotted currentColor;margin:0 2px 3px}
.note{font-size:7px;line-height:11px}
.dark{background:var(--slate);color:#fff}
.nails-menu{position:absolute;left:21px;right:36px;top:22px}
.feet-photo{left:0;top:370px;width:250px;height:160px;background:linear-gradient(160deg,#f6ecea,#e8cfc7 55%,#d3aea4)}

.logo-ring--small{left:85px;top:16px;width:80px;height:80px}
.logo-ring--small .brand{font-size:17px}
.facials{position:absolute;left:26px;right:34px;top:118px}
.treat{margin-bottom:9px}
.treat .name{color:var(--rosegold)}
.eyes-title{margin-top:4px}
.portrait{left:0;top:0;width:249px;height:280px;background:linear-gradient(160deg,#f4eeec,#d9bfb2 45%,#8d6c5f)}
.body-menu{position:absolute;left:26px;right:26px;top:296px}
.body-menu .menu-title{margin-bottom:2px}
.body-menu .group{margin-bottom:10px}
</style>
</head>
<body>

<section class="sheet sheet--outside">
  <div class="panel panel--1">
    <h2 class="about-title script">About us</h2>
    <p class="about-copy about-copy--a">Lumen Nails &amp; Beauty is a modern salon located in the town centre of beautiful Kiriwai. Offering Facials, Waxing, Tinting and Nails this is your one stop shop for all your beauty needs! Lumen uses only the best products available to ensure that every client is getting what they deserve.</p>
    <p class="about-copy about-copy--b">The PolishHouse Co™ gel polishes are rich, highly pigmented, chip-resistant and offer extreme long lasting shine. The good news doesn’t end there because PolishHouse is VEGAN, CRUELTY FREE and 10-FREE (our products don’t contain formaldehyde, Dibutyl phthalate, toluene, formaldehyde resin or camphor).</p>
    <div class="photo about-photo" role="img" aria-label="Photo of a manicure being given at a salon table"></div>
    <svg class="photo" style="left:0;top:300px" width="250" height="80" viewBox="0 0 250 80" aria-hidden="true">
      <path d="M0 80 C40 40 120 30 250 50 L250 36 C120 14 40 24 0 62 Z" fill="#d8aba0"/>
      <path d="M0 62 C40 24 120 14 250 36 L250 0 L0 0 Z" fill="#ffffff"/>
    </svg>
    <div class="ring ring--nails" role="img" aria-label="Close photo of manicured nails"></div>
    <div class="ring ring--eyes" role="img" aria-label="Close photo of eyes with under-eye patches"></div>
  </div>

  <div class="panel panel--2 outside">
    <svg class="photo" style="left:0;top:0" width="250" height="530" viewBox="0 0 250 530" aria-hidden="true">
      <path d="M0 0 L250 0 L250 70 C170 40 70 14 0 0 Z" fill="#ffffff"/>
      <path d="M0 6 C70 22 170 48 250 78 L250 70 C170 40 70 14 0 0 Z" fill="#d8aba0"/>
      <path d="M0 345 C80 335 170 380 250 402 L250 530 L0 530 Z" fill="#67636a"/>
      <path d="M0 335 C80 325 170 372 250 396 L250 402 C170 380 80 335 0 345 Z" fill="#d8aba0"/>
    </svg>
    <div class="logo-ring"><span class="brand">Lumen</span><small>Nails &amp; Beauty</small></div>
    <div class="quote-mark">“</div>
    <p class="testimonial">I absolutely loved every single second of my facial with Karen. I left the salon feeling so relaxed and my skin smooth and glowing. I can’t wait for my next appointment.</p>
    <h2 class="call-title script">call us today</h2>
    <div class="pill pill--phone">
      <svg width="9" height="9" viewBox="0 0 10 10" aria-hidden="true"><circle cx="5" cy="5" r="4.4" fill="none" stroke="#3d3a3f" stroke-width=".9"/><path d="M3.3 2.8l1 1-.5.6c.3.6.8 1.1 1.4 1.4l.6-.5 1 1-.6.7C4.8 6.9 3.1 5.2 2.7 3.4z" fill="#3d3a3f"/></svg>
      0273816240
    </div>
    <div class="email">Karen.lumen@mailbox.test</div>
    <address class="address">Lumen Nails &amp; Beauty<br>Karen Pell<br>Room3, 48 Tainui Street<br>Kiriwai</address>
    <div class="socials">
      <span class="social"><i></i>Chatterly @lumenbeauty</span>
      <span class="social"><i></i>Snapgrid @lumenbeauty</span>
    </div>
    <div class="pill pill--web">www.lumenbeauty.co.nz</div>
  </div>

  <div class="panel panel--3 dark">
    <div class="photo" style="left:0;top:0;width:249px;height:100px;background:#fff"></div>
    <div class="cover-logo"><span class="brand">Lumen</span><small>Nails &amp; Beauty</small></div>
    <div class="photo cover-photo" role="img" aria-label="Beauty portrait of a woman with pink lips and manicured nails"></div>
    <svg class="photo" style="left:0;top:70px" width="249" height="360" viewBox="0 0 249 360" aria-hidden="true">
      <path d="M0 26 C80 -2 170 4 249 -4 L249 6 C170 16 80 12 0 36 Z" fill="#d8aba0"/>
      <path d="M0 360 L0 350 C90 340 200 300 249 240 L249 360 Z" fill="#67636a"/>
      <path d="M0 340 C90 330 200 290 249 228 L249 240 C200 300 90 340 0 350 Z" fill="#d8aba0"/>
    </svg>
    <div class="cover-title">Nails &amp; Beauty</div>
    <div class="pill pill--web">www.lumenbeauty.co.nz</div>
  </div>
</section>

<section class="sheet sheet--inside">
  <div class="panel panel--1 dark">
    <div class="nails-menu">
      <h2 class="menu-title script">Nails</h2>
      <div class="menu-head">Manicure</div>
      <div class="row">Gel Polish<span class="dots"></span>$45</div>
      <div class="row">Regular Polish<span class="dots"></span>$40</div>
      <div class="menu-head">Pedicure</div>
      <div class="row">Gel Polish<span class="dots"></span>$45</div>
      <div class="row">Regular Polish<span class="dots"></span>$40</div>
      <div class="menu-head" style="margin-bottom:0">Luxury Pedicure</div>
      <div class="note">Includes: soak, exfoliation, heel rasping &amp; massage</div>
      <div style="height:7px"></div>
      <div class="row">Gel Polish<span class="dots"></span>$60</div>
      <div class="row">Regular Polish<span class="dots"></span>$55</div>
      <div class="menu-head" style="display:flex;white-space:nowrap">Gel Removal &amp; Nail Tidy<span style="flex:1;border-bottom:1px dotted currentColor;margin:0 2px 3px"></span>$25</div>
      <div class="menu-head">Add On</div>
      <div class="row">Gel Removal<span class="dots"></span>$5</div>
      <div class="row">Base Build<span class="dots"></span>$5 per layer</div>
      <div class="row">Strength gel<span class="dots"></span>$10</div>
      <div class="row">Nail Art/ Glitter | SPOA</div>
    </div>
    <div class="photo feet-photo" role="img" aria-label="Photo of pedicured feet and manicured hands with flowers"></div>
    <svg class="photo" style="left:0;top:355px" width="250" height="50" viewBox="0 0 250 50" aria-hidden="true">
      <path d="M0 0 L250 0 L250 50 C180 18 80 4 0 18 Z" fill="#67636a"/>
      <path d="M0 18 C80 4 180 18 250 50 L250 42 C180 10 80 -2 0 10 Z" fill="#d8aba0"/>
    </svg>
  </div>

  <div class="panel panel--2" style="background:linear-gradient(90deg,#f1f0f0,#fff 20%,#fff 80%,#f1f0f0)">
    <div class="logo-ring logo-ring--small"><span class="brand">Lumen</span><small>Nails &amp; Beauty</small></div>
    <div class="facials">
      <h2 class="menu-title script">Facials</h2>
      <div class="treat"><div class="row"><span class="name">Deep Cleansing Facial</span><span class="dots"></span>$75</div><div class="note">49 minutes<br>Removes build up of dead skin cells, leaves the skin feeling soft and hydrated.</div></div>
      <div class="treat"><div class="row"><span class="name">Therapeutic Facial</span><span class="dots"></span>$105</div><div class="note">60 minutes<br>Tailored to suit your skins specific needs.</div></div>
      <div class="treat"><div class="row"><span class="name">Rejuvenation Facial</span><span class="dots"></span>$120</div><div class="note">60 Minutes<br>Active yet gentle treatment that facilitates dermal rejuvenation.</div></div>
      <div class="treat"><div class="row"><span class="name">35% Glycolic Facial</span><span class="dots"></span>$120</div><div class="note">60 Minutes<br>Hydrating, deep exfoliation treatment improving skin texture and appearance.</div></div>
      <div class="treat"><div class="row"><span class="name">Dermaplaning</span><span class="dots"></span>$120</div><div class="note">Creates a smooth and radiant skin surface. Also removes soft facial hairs.</div></div>
      <h2 class="menu-title script eyes-title">Eyes</h2>
      <div class="row">Lash Lift<span class="dots"></span>$115</div>
      <div class="row">Eyebrow Shape<span class="dots"></span>$19</div>
      <div class="row">Eyebrow Tint<span class="dots"></span>$18</div>
      <div class="row">Eyelash Tint<span class="dots"></span>$25</div>
      <div class="row">Eye Trio<span class="dots"></span>$45</div>
    </div>
  </div>

  <div class="panel panel--3 dark">
    <div class="photo portrait" role="img" aria-label="Portrait of a woman with smooth skin and long brown hair"></div>
    <svg class="photo" style="left:0;top:160px" width="249" height="140" viewBox="0 0 249 140" aria-hidden="true">
      <path d="M0 140 L0 112 C90 110 190 80 249 20 L249 140 Z" fill="#67636a"/>
      <path d="M0 104 C90 102 190 72 249 10 L249 20 C190 80 90 110 0 112 Z" fill="#d8aba0"/>
    </svg>
    <div class="body-menu">
      <div class="group">
        <h2 class="menu-title script">Face</h2>
        <div class="row">Lip<span class="dots"></span>$15</div>
        <div class="row">Chin<span class="dots"></span>$15</div>
      </div>
      <div class="group">
        <h2 class="menu-title script">Body</h2>
        <div class="row">Under Arm<span class="dots"></span>$20</div>
        <div class="row">1/2 Leg<span class="dots"></span>$35</div>
        <div class="row">Full Leg<span class="dots"></span>$55</div>
        <div class="row">1/2 Arm<span class="dots"></span>$30</div>
        <div class="row">Full Arm<span class="dots"></span>$40</div>
        <div class="row">Bikini<span class="dots"></span>$28</div>
        <div class="row">Extended Bikini<span class="dots"></span>$38</div>
        <div class="row">Brazilian (1st Time)<span class="dots"></span>$65</div>
        <div class="row">Brazilian (4-6 Weeks)<span class="dots"></span>$50</div>
        <div class="row">Patches<span class="dots"></span>$5</div>
      </div>
    </div>
  </div>
</section>

</body>
</html>
```